Tallow Bodyweight Gym Website

We need a website design for our gym.

Tallow is the UAE's first calisthenics and parkour gym. The theme under which the gym revolves is that one does not require any machinery to workout as our bodies could be themselves the machinery. The gym is designed to be the more of a social hub rather than an "in-and-out" gym, where people come train, have fun, hang out and socialize for a few hours rather than just train for 60 minutes then leave. The gym is designed to be a big open space with lots of natural sunlight, natural wood and plants all over the place to create a natural and refreshing setting. We also use recycled material throughout the gym and recycle our waste as being green is part of our philosophy. We currently also have some of the world's top and most recognized calisthenics athletes working with us.

We would like our website to reflect all that as well as provide a simple, interactive and fun way for visitors to be able to get class and gym information, check out gym media and contact us for bookings.

Target Market(s)

Ages 15-35

Industry/Entity Type

Fitness

Coding

Coded - Design and coding required

Number of Pages Required

4 page

Font styles to use
Decorative

Colors
0792cd

Requirements
Must have
• Class descriptions
• Gym description
• Class schedules
• Trainer profiles
• Gym philosophy
• Contact Details
Nice to have
• A link to contact us directly for a free first trial class

```html
<!DOCTYPE html>
<html lang="en">
<head>
<meta charset="utf-8">
<title>Tallow Bodyweight Gym – Class Schedule</title>
<link href="https://fonts.googleapis.com/css2?family=Open+Sans:ital,wght@0,400;0,600;0,700;0,800;1,400;1,700;1,800&display=swap" rel="stylesheet">
<style>
:root{
  --blue:#0792cd;
  --blue-dark:#0a7fb3;
  --footer-bar:#0580bb;
  --ink:#333;
  --ink-soft:#555;
  --line:#e2e2e2;
  --page-grey:#f0f0f0;
  --band-grey:#e5e5e5;
  --green:#4aa86a;
  --btn-green:#13700f;
  --btn-red:#ee1c1c;
  --navy:#16283a;
  --white:#fff;
}
*{box-sizing:border-box;margin:0;padding:0}
html,body{width:1200px;height:2995px;overflow:hidden}
body{position:relative;background:var(--page-grey);font-family:"Open Sans",Arial,sans-serif;color:var(--ink)}
.abs{position:absolute}

/* header */
.site-header{left:0;top:0;width:1200px;height:136px;background:var(--white)}
.brand{left:106px;top:36px}
.brand-name{font-size:26px;font-weight:600;color:var(--blue);line-height:1.2;white-space:nowrap}
.topbar{right:82px;top:24px;display:flex;align-items:center;gap:6px}
.phone-icon{width:22px;height:22px;background:var(--blue);display:flex;align-items:center;justify-content:center;margin-right:4px}
.phone-num{font-size:14px;color:var(--ink-soft);margin-right:16px}
.social-sq{width:20px;height:20px;background:var(--blue)}
.main-nav{right:82px;top:82px;display:flex;gap:37px;font-size:13px;font-weight:600;color:var(--blue);text-transform:uppercase}

/* hero */
.hero{left:0;top:136px;width:1200px;height:210px;background:linear-gradient(90deg,#7a4f2c 0%,#9a6a3e 20%,#5d6b2f 40%,#8b5f35 60%,#6f7a3a 75%,#3a3a3a 100%)}
.hero-tab{left:106px;top:306px;width:320px;height:40px;background:var(--blue);color:var(--white);font-size:26px;line-height:40px;padding-left:46px;text-transform:uppercase}

/* schedule */
.class-filter{left:0;top:406px;width:1200px;display:flex;justify-content:center;gap:6px;font-size:12px;font-weight:600;color:var(--blue);text-transform:uppercase}
.class-filter span{padding:7px 14px;border:1px solid transparent}
.class-filter .active{border-color:var(--blue);background:var(--white)}
.schedule{left:94px;top:468px;width:1016px;border-collapse:collapse;table-layout:fixed;background:var(--white);font-size:11px}
.schedule th,.schedule td{border:1px solid var(--line);text-align:center;vertical-align:middle}
.schedule th{height:44px;font-weight:700;color:var(--ink);font-size:11px;text-transform:uppercase}
.schedule td.time{color:var(--ink-soft);font-size:11px}
.schedule td.ev{background:var(--blue);color:var(--white);border-color:var(--blue);font-weight:700;line-height:1.5}
.schedule td.ev small{display:block;font-weight:400;font-size:11px}

/* trainers + blog */
.section-title{font-size:21px;font-weight:600;color:var(--blue);text-transform:uppercase}
.trainers-title{left:94px;top:1506px}
.blog-title{left:788px;top:1506px}
.trainers{left:94px;top:1552px;width:668px;height:276px;background:var(--white)}
.trainer{position:absolute;top:20px;width:160px;margin-left:-80px;text-align:center}
.trainer-photo{width:96px;height:96px;border-radius:50%;margin:0 auto 44px;background:linear-gradient(135deg,#c9d3dc,#8c6b5a)}
.trainer-name{font-size:14px;color:var(--blue);text-transform:uppercase;line-height:1.2}
.trainer-role{font-size:12px;font-style:italic;color:#8ac9e6;text-transform:uppercase;line-height:1.4}
.trainer-bio{font-size:11px;font-style:italic;color:var(--ink-soft);line-height:1.4;margin-top:4px}
.trainer-meta{display:flex;justify-content:space-between;align-items:center;margin-top:10px;padding:0 6px}
.dots{display:flex;gap:5px}
.dots i{width:8px;height:8px;background:var(--blue);border-radius:50%;display:block}
.carousel-arrow{top:114px}
.blog{left:788px;top:1552px;width:322px;height:264px;background:var(--green);padding:16px}
.post{display:flex;gap:16px;margin-bottom:14px;color:var(--white)}
.post-thumb{width:70px;height:64px;flex:none;background:linear-gradient(135deg,#e8e8e8,#9a7c6a);border:2px solid var(--white)}
.post p{font-size:11px;line-height:1.45}

/* join band */
.join-band{left:0;top:1898px;width:1200px;height:284px;background:var(--blue);color:var(--white)}
.join-col{position:absolute;top:64px;width:400px;text-align:center}
.join-col h2{font-size:29px;font-weight:800;font-style:italic;text-transform:uppercase;line-height:1.1}
.join-col h3{font-size:18px;font-weight:700;margin-top:8px}
.join-col p{font-size:12px;line-height:1.55;margin:8px auto 0;width:370px}
.join-divider{left:588px;top:66px;width:1px;height:150px;background:rgba(255,255,255,.6)}
.btn{display:inline-flex;align-items:center;justify-content:center;font-size:12px;text-transform:uppercase;height:38px}
.btn-red{background:var(--btn-red);color:var(--white);width:208px;margin-top:20px}
.btn-white{background:var(--white);color:var(--blue);width:120px}
.btn-green{background:var(--btn-green);color:var(--white);width:134px}
.account h2,.account h3{color:var(--navy)}

/* gallery */
.gallery-band{left:0;top:2182px;width:1200px;height:520px;background:var(--band-grey)}
.gallery-title{left:0;top:2228px;width:1200px;text-align:center;font-size:21px;font-weight:600;color:var(--blue)}
.gallery{left:0;top:2278px;width:1200px;height:358px;display:grid;grid-template-columns:276px 276px 276px 276px 80px;grid-template-rows:176px 176px;gap:6px 4px}
.shot{background:linear-gradient(160deg,#8a6a44,#5e7a3a 55%,#444)}
.shot.room{background:linear-gradient(170deg,#e9ecee,#b8c2c8 60%,#6d7b84)}
.gallery-arrow{top:2436px;width:44px;height:44px;border-radius:50%;background:rgba(255,255,255,.7);display:flex;align-items:center;justify-content:center}

/* footer */
.site-footer{left:0;top:2702px;width:1200px;height:258px;background:var(--blue);color:var(--white)}
.footer-bar{left:0;top:2960px;width:1200px;height:35px;background:var(--footer-bar);color:var(--white);font-size:11px}
.newsletter{left:94px;top:50px;width:300px}
.footer-h{font-size:15px;text-transform:uppercase;font-weight:400;margin-bottom:10px}
.newsletter p{font-size:12px;line-height:1.5;text-transform:uppercase}
.email-input{margin-top:16px;width:284px;height:34px;background:#7fcdf0;color:var(--white);font-size:11px;line-height:34px;padding-left:14px;text-transform:uppercase}
.email-btn{margin-top:14px;width:158px;height:38px;border:2px solid var(--white);font-size:14px;font-weight:700;display:flex;align-items:center;justify-content:center;gap:10px;text-transform:uppercase}
.footer-info{left:442px;top:32px;width:340px;font-size:12px;line-height:1.65}
.contact-line{margin-top:16px;display:flex;gap:14px;align-items:baseline}
.contact-line b{font-size:15px;font-style:italic;font-weight:700}
.footer-menu{top:50px}
.footer-menu ul{list-style:none;font-size:12px;line-height:22px}
.footer-menu li::before{content:"›";margin-right:10px}
</style>
</head>
<body>

<header class="site-header abs">
  <div class="brand abs">
    <span class="brand-name">Tallow Bodyweight Gym</span>
  </div>
  <div class="topbar abs">
    <span class="phone-icon">
      <svg width="12" height="12" viewBox="0 0 24 24"><path fill="#fff" d="M6.6 10.8a15.2 15.2 0 0 0 6.6 6.6l2.2-2.2c.3-.3.7-.4 1-.2 1.1.4 2.3.6 3.6.6.6 0 1 .4 1 1V20c0 .6-.4 1-1 1A17 17 0 0 1 3 4c0-.6.4-1 1-1h3.5c.6 0 1 .4 1 1 0 1.3.2 2.5.6 3.6.1.3 0 .7-.2 1z"/></svg>
    </span>
    <span class="phone-num">1-200-555-0142</span>
    <span class="social-sq"></span><span class="social-sq"></span><span class="social-sq"></span><span class="social-sq"></span>
  </div>
  <nav class="main-nav abs">
    <span>Home</span><span>About</span><span>Trainers</span><span>Classes</span><span>Blog</span><span>Pricing</span><span>Contact</span>
  </nav>
</header>

<div class="hero abs" role="img" aria-label="Living plant wall lettering on natural wood panels, with a dumbbell rack and exercise balls"></div>
<div class="hero-tab abs">Class Schedule</div>

<div class="class-filter abs">
  <span class="active">All Classes</span><span>Gym Class</span><span>Yoga Class</span><span>Lorem Class</span><span>Ipsum Class</span><span>Dolor Class</span>
</div>

<table class="schedule abs">
  <colgroup><col style="width:126px"><col span="7" style="width:127px"></colgroup>
  <thead><tr><th></th><th>Monday</th><th>Tuesday</th><th>Wednesday</th><th>Thursday</th><th>Friday</th><th>Saturday</th><th>Sunday</th></tr></thead>
  <tbody>
    <tr style="height:66px"><td class="time">05.00 - 06.00</td><td class="ev">Lorem<small>05.00 - 06.00</small></td><td class="ev">Boxing<small>05.00 - 06.00</small></td><td></td><td></td><td></td><td></td><td></td></tr>
    <tr style="height:66px"><td class="time">06.00 - 07.00</td><td class="ev">Gym Fitness<small>06.00 - 07.00</small></td><td class="ev">Gym Fitness<small>06.00 - 07.00</small></td><td class="ev">Gym Fitness<small>06.00 - 08.30</small></td><td class="ev">Gym Fitness<small>06.00 - 08.30</small></td><td class="ev">Gym Fitness<small>06.00 - 08.30</small></td><td></td><td></td></tr>
    <tr style="height:64px"><td class="time">07.00 - 08.00</td><td class="ev">Cardio Fitness<small>07.00 - 08.00</small></td><td class="ev">Cardio Fitness<small>07.00 - 08.00</small></td><td class="ev">Cardio Fitness<small>06.00 - 08.30</small></td><td class="ev">Cardio Fitness<small>06.00 - 08.30</small></td><td class="ev">Cardio Fitness<small>06.00 - 08.30</small></td><td></td><td></td></tr>
    <tr style="height:46px"><td class="time">08.00 - 09.00</td><td></td><td></td><td></td><td></td><td></td><td class="ev" rowspan="2">Indoor Cycling<small>08.00 - 09.30</small></td><td class="ev" rowspan="2">Indoor Cycling<small>08.00 - 09.30</small></td></tr>
    <tr style="height:64px"><td class="time">09.00 - 10.00</td><td class="ev" rowspan="3">Indoor Cycling<small>09.00 - 11.25</small></td><td class="ev" rowspan="3">Indoor Cycling<small>09.00 - 11.25</small></td><td></td><td class="ev">Indoor Cycling<small>09.00 - 10.00</small></td><td class="ev">Indoor Cycling<small>09.00 - 10.00</small></td></tr>
    <tr style="height:66px"><td class="time">10.00 - 11.00</td><td></td><td class="ev" rowspan="2">Cardio Fitness<small>10.00 - 11.30</small></td><td class="ev" rowspan="2">Cardio Fitness<small>10.00 - 11.30</small></td><td class="ev">Gym Fitness<small>10.00 - 11.00</small></td><td class="ev">Gym Fitness<small>10.00 - 11.00</small></td></tr>
    <tr style="height:66px"><td class="time">11.00 - 12.00</td><td></td><td class="ev">Indoor Cycling<small>11.00 - 12.00</small></td><td class="ev">Indoor Cycling<small>11.00 - 12.00</small></td></tr>
    <tr style="height:66px"><td class="time">12.00 - 13.00</td><td></td><td></td><td class="ev">Gym Fitness<small>12.00 - 13.00</small></td><td class="ev">Gym Fitness<small>12.00 - 13.00</small></td><td class="ev" rowspan="4">Boxing<small>12.00 - 15.45</small></td><td class="ev">Gym Fitness<small>12.00 - 13.00</small></td><td class="ev">Gym Fitness<small>12.00 - 13.00</small></td></tr>
    <tr style="height:44px"><td class="time">13.00 - 14.00</td><td></td><td></td><td></td><td></td><td class="ev">Boxing<small>12.00 - 15.45</small></td><td></td></tr>
    <tr style="height:44px"><td class="time">14.00 - 15.00</td><td class="ev" rowspan="2">Gym Fitness<small>14.00 - 16.15</small></td><td class="ev" rowspan="2">Gym Fitness<small>14.00 - 16.15</small></td><td></td><td></td><td class="ev" rowspan="2">Cardio Fitness<small>14.00 - 16.00</small></td><td class="ev" rowspan="2">Cardio Fitness<small>14.00 - 16.00</small></td></tr>
    <tr style="height:48px"><td class="time">15.00 - 16.00</td><td></td><td></td></tr>
    <tr style="height:44px"><td class="time">16.00 - 17.00</td><td class="ev" rowspan="2">Indoor Cycling<small>16.00 - 17.30</small></td><td class="ev" rowspan="2">Indoor Cycling<small>16.00 - 17.30</small></td><td></td><td class="ev" rowspan="2">Indoor Cycling<small>16.00 - 17.30</small></td><td class="ev">Indoor Cycling<small>16.00 - 17.30</small></td><td></td><td></td></tr>
    <tr style="height:66px"><td class="time">17.00 - 18.00</td><td></td><td class="ev">Gym Fitness<small>17.30 - 18.00</small></td><td class="ev">Gym Fitness<small>17.00 - 18.00</small></td><td class="ev">Gym Fitness<small>17.00 - 18.00</small></td></tr>
    <tr style="height:60px"><td class="time">18.00 - 19.00</td><td class="ev">Lorem<small>18.00 - 19.00</small></td><td class="ev">Lorem<small>18.00 - 19.00</small></td><td class="ev">Lorem<small>18.00 - 20.00</small></td><td class="ev">Lorem<small>18.00 - 20.00</small></td><td class="ev" rowspan="2">Boxing<small>18.00 - 20.00</small></td><td></td><td></td></tr>
    <tr style="height:60px"><td class="time">19.00 - 20.00</td><td class="ev">Yoga Pilates<small>18.30 - 20.00</small></td><td class="ev">Yoga Pilates<small>18.30 - 20.00</small></td><td class="ev">Yoga Pilates<small>18.30 - 20.00</small></td><td class="ev">Yoga Pilates<small>18.30 - 20.00</small></td><td class="ev" rowspan="2">Yoga Pilates<small>19.00 - 20.30</small></td><td class="ev" rowspan="2">Yoga Pilates<small>19.00 - 20.30</small></td></tr>
    <tr style="height:46px"><td class="time">20.00 - 21.00</td><td></td><td></td><td></td><td></td><td></td></tr>
  </tbody>
</table>

<h2 class="section-title trainers-title abs">Our Trainers</h2>
<h2 class="section-title blog-title abs">From the Blog</h2>

<section class="trainers abs">
  <svg class="carousel-arrow abs" style="left:18px" width="14" height="26" viewBox="0 0 14 26"><path d="M12 2 2 13l10 11" fill="none" stroke="#8ac9e6" stroke-width="2"/></svg>
  <svg class="carousel-arrow abs" style="left:638px" width="14" height="26" viewBox="0 0 14 26"><path d="M2 2l10 11L2 24" fill="none" stroke="#8ac9e6" stroke-width="2"/></svg>

  <div class="trainer" style="left:108px">
    <div class="trainer-photo" role="img" aria-label="Trainer portrait"></div>
    <div class="trainer-name">Lorem Ipsum</div><div class="trainer-role">Kik Boxing</div>
    <div class="trainer-bio">Lorem ipsum dolor<br>sit amet, consectetuer.</div>
    <div class="trainer-meta"><svg width="14" height="12" viewBox="0 0 24 22"><path fill="#bbb" d="M12 21 2 11a6 6 0 0 1 10-7 6 6 0 0 1 10 7z"/></svg><span class="dots"><i></i><i></i></span></div>
  </div>
  <div class="trainer" style="left:264px">
    <div class="trainer-photo" role="img" aria-label="Trainer portrait"></div>
    <div class="trainer-name">Lorem Ipsum</div><div class="trainer-role">Spinning</div>
    <div class="trainer-bio">Lorem ipsum dolor<br>sit amet, consectetuer.</div>
    <div class="trainer-meta"><svg width="14" height="12" viewBox="0 0 24 22"><path fill="#bbb" d="M12 21 2 11a6 6 0 0 1 10-7 6 6 0 0 1 10 7z"/></svg><span class="dots"><i></i><i></i></span></div>
  </div>
  <div class="trainer" style="left:424px">
    <div class="trainer-photo" role="img" aria-label="Trainer portrait"></div>
    <div class="trainer-name">Lorem Ipsum</div><div class="trainer-role">Spinning</div>
    <div class="trainer-bio">Lorem ipsum dolor<br>sit amet, consectetuer.</div>
    <div class="trainer-meta"><svg width="14" height="12" viewBox="0 0 24 22"><path fill="#e31e24" d="M12 21 2 11a6 6 0 0 1 10-7 6 6 0 0 1 10 7z"/></svg><span class="dots"><i></i><i></i></span></div>
  </div>
  <div class="trainer" style="left:584px">
    <div class="trainer-photo" role="img" aria-label="Trainer portrait"></div>
    <div class="trainer-name">Lorem Ipsum</div><div class="trainer-role">Kik Boxing</div>
    <div class="trainer-bio">Lorem ipsum dolor<br>sit amet, consectetuer.</div>
    <div class="trainer-meta"><svg width="14" height="12" viewBox="0 0 24 22"><path fill="#bbb" d="M12 21 2 11a6 6 0 0 1 10-7 6 6 0 0 1 10 7z"/></svg><span class="dots"><i></i><i></i></span></div>
  </div>
</section>

<section class="blog abs">
  <article class="post"><div class="post-thumb" role="img" aria-label="Training photo"></div><p>nostrud exerci tation ullamcorper suscipit lobortis nisl ut aliquip<br>25 April, 2014</p></article>
  <article class="post"><div class="post-thumb" role="img" aria-label="Training photo"></div><p>soluta nobis eleifend option congue nihil imperdiet doming id<br>25 April, 2014</p></article>
  <article class="post"><div class="post-thumb" role="img" aria-label="Training photo"></div><p>quod mazim placerat facer possim assum. Typi non habent<br>25 April, 2014</p></article>
</section>

<section class="join-band abs">
  <div class="join-col" style="left:190px">
    <h2>Why not join ?</h2>
    <h3>Sed diam nonummy nibh euismod</h3>
    <p>Lorem ipsum dolor sit amet, consectetuer adipiscing elit, sed diam nibh euismod tincidunt ut laoreet dolore magna .</p>
    <span class="btn btn-red">Join Today</span>
  </div>
  <div class="join-divider abs"></div>
  <div class="join-col account" style="left:630px">
    <h2>Have account ?</h2>
    <h3>Sed diam nonummy nibh euismod</h3>
    <p>Lorem ipsum dolor sit amet, consectetuer adipiscing elit, sed diam nibh euismod tincidunt ut laoreet dolore magna .</p>
    <div style="margin-top:28px;display:flex;justify-content:center;gap:26px"><span class="btn btn-white">Log In</span><span class="btn btn-green">View Calender</span></div>
  </div>
</section>

<div class="gallery-band abs"></div>
<h2 class="gallery-title abs">GALLERY</h2>
<div class="gallery abs">
  <div class="shot" role="img" aria-label="Plant wall lettering above dumbbell rack"></div>
  <div class="shot" role="img" aria-label="Plant wall lettering above dumbbell rack"></div>
  <div class="shot room" role="img" aria-label="Open training floor with calisthenics rig"></div>
  <div class="shot" role="img" aria-label="Plant wall lettering above dumbbell rack"></div>
  <div class="shot" role="img" aria-label="Plant wall lettering above dumbbell rack"></div>
  <div class="shot room" role="img" aria-label="Gymnastic rings hanging from a rig"></div>
  <div class="shot room" role="img" aria-label="Open training floor with calisthenics rig"></div>
  <div class="shot room" role="img" aria-label="Open training floor with calisthenics rig"></div>
  <div class="shot room" role="img" aria-label="Open training floor with calisthenics rig"></div>
  <div class="shot room" role="img" aria-label="Open training floor with calisthenics rig"></div>
</div>
<div class="gallery-arrow abs" style="left:14px"><svg width="12" height="18" viewBox="0 0 12 18"><path d="M10 2 3 9l7 7" fill="none" stroke="#888" stroke-width="2"/></svg></div>
<div class="gallery-arrow abs" style="left:1142px"><svg width="12" height="18" viewBox="0 0 12 18"><path d="M2 2l7 7-7 7" fill="none" stroke="#888" stroke-width="2"/></svg></div>

<footer class="site-footer abs">
  <div class="newsletter abs">
    <h4 class="footer-h">Newsletter Signup</h4>
    <p>Lorem ipsum dolor sit amet, consectetuer adipiscing elit sed diam nonummy.</p>
    <div class="email-input">Insert Email</div>
    <div class="email-btn">Submit Email <svg width="8" height="12" viewBox="0 0 8 12"><path d="M1 1l5 5-5 5" fill="none" stroke="#fff" stroke-width="2"/></svg></div>
  </div>
  <div class="footer-info abs">
    <p>Lorem ipsum dolor sit amet, consectetuer adipiscing elit, sed diam nonummy nibh euismod tincidunt ut laoreet dolore magna aliquam erat volutpat. Ut wisi enim ad minim veniam, quis</p>
    <div class="contact-line"><span>Phone :</span><b>(00) 222 666 444</b></div>
    <div class="contact-line" style="margin-top:10px"><span>Email :</span><b>youremail@yourdomain.com</b></div>
  </div>
  <div class="footer-menu abs" style="left:824px">
    <h4 class="footer-h">Menu</h4>
    <ul><li>About</li><li>Trainers</li><li>Classes</li><li>Pricing</li><li>Privacy</li><li>Contact</li></ul>
  </div>
  <div class="footer-menu abs" style="left:984px">
    <h4 class="footer-h">Community</h4>
    <ul><li>Blog</li><li>Forum</li><li>Support</li><li>Newsletter</li></ul>
  </div>
</footer>
<div class="footer-bar abs">
  <span class="abs" style="left:94px;top:10px">© 2014 Template by Tallow Bodyweight Gym</span>
  <span class="abs" style="left:1012px;top:8px;display:flex;gap:6px"><span class="social-sq" style="background:#fff;opacity:.25"></span><span class="social-sq" style="background:#fff;opacity:.25"></span><span class="social-sq" style="background:#fff;opacity:.25"></span><span class="social-sq" style="background:#fff;opacity:.25"></span></span>
</div>

</body>
</html>
```